Small but growing painting company. Have built up a steady client base. Want to start having a more professional look. Want to start with changing my business cards, and also getting new logo and tee shirts.

Target Market(s)

Home owners, property management companies, all ages 30-70

Industry/Entity Type

Painting And Decorating

Contact Information for Business Card

Bright Ridge Painting LLC Derek Vanstrand 630-485-7039 interior, exterior, vaulted ceiling, drywall repair, pressure washing, kitchen cabinets, epoxy, garage floors,

Font styles to use
Sans Serif
Other font styles liked:
• Harrington

Colors
0355a3
ffffff
ec1f27
000000
3176b5
0493ce
474747
b7b7b7

Requirements
Must have
• Creative, something that doesn’t look like every other painting card.
Nice to have
• I would like something with an arrow or something going to a point

```html
<!DOCTYPE html>
<html lang="en">
<head>
<meta charset="utf-8">
<title>Bright Ridge Painting — Business Card</title>
<link href="https://fonts.googleapis.com/css2?family=Montserrat:wght@500;600;800&display=swap" rel="stylesheet">
<style>
  :root {
    --brand-red: #ec1f27;
    --ink-grey: #474747;
    --rule-grey: #3a3a3a;
    --paper: #ffffff;
    --backdrop: #e9e6e1;
    --card-shadow: rgba(0, 0, 0, 0.22);
  }
  * { box-sizing: border-box; margin: 0; padding: 0; }
  html, body {
    width: 1200px;
    height: 1000px;
    overflow: hidden;
    background: var(--backdrop);
    font-family: "Montserrat", Arial, sans-serif;
  }
  .stage {
    position: relative;
    width: 1200px;
    height: 1000px;
  }
  .card {
    position: absolute;
    width: 630px;
    height: 360px;
    border-radius: 34px;
    box-shadow: 0 14px 30px var(--card-shadow);
    overflow: hidden;
  }
  /* Front side */
  .card-front {
    left: 150px;
    top: 90px;
    background: var(--brand-red);
    display: flex;
    align-items: center;
    justify-content: center;
  }
  .front-wordmark {
    color: var(--paper);
    font-weight: 800;
    font-size: 50px;
    line-height: 1.05;
    text-align: center;
    letter-spacing: 0.5px;
  }
  /* Back side */
  .card-back {
    left: 420px;
    top: 540px;
    background: var(--paper);
    display: flex;
  }
  .contact-panel {
    width: 330px;
    padding: 120px 0 0 38px;
  }
  .back-wordmark {
    color: var(--ink-grey);
    font-weight: 800;
    font-size: 33px;
    line-height: 1.05;
  }
  .person-name {
    margin-top: 26px;
    color: var(--ink-grey);
    font-weight: 600;
    font-size: 23px;
  }
  .person-phone {
    margin-top: 10px;
    color: var(--brand-red);
    font-weight: 600;
    font-size: 23px;
    letter-spacing: 0.5px;
  }
  .divider {
    width: 2px;
    margin: 46px 0 40px;
    background: var(--rule-grey);
  }
  .services {
    list-style: none;
    padding: 40px 0 0 24px;
  }
  .services li {
    position: relative;
    padding-left: 20px;
    color: var(--ink-grey);
    font-weight: 500;
    font-size: 21px;
    line-height: 31px;
  }
  .services li::before {
    content: "";
    position: absolute;
    left: 0;
    top: 12px;
    width: 9px;
    height: 9px;
    border-radius: 50%;
    background: var(--brand-red);
  }
</style>
</head>
<body>
  <main class="stage">
    <section class="card card-front" aria-label="Business card front">
      <div class="front-wordmark">Bright Ridge<br>PAINTING</div>
    </section>

    <section class="card card-back" aria-label="Business card back">
      <div class="contact-panel">
        <div class="back-wordmark">Bright Ridge<br>PAINTING</div>
        <p class="person-name">Derek Vanstrand</p>
        <p class="person-phone">630-485-7039</p>
      </div>
      <div class="divider"></div>
      <ul class="services">
        <li>interior</li>
        <li>exterior</li>
        <li>vaulted ceiling</li>
        <li>drywall repair</li>
        <li>pressure washing</li>
        <li>kitchen cabinets</li>
        <li>epoxy</li>
        <li>garage floors</li>
      </ul>
    </section>
  </main>
</body>
</html>
```